Landing Page for our Applicants Page

Landing Page for the applicants for our QV campaign and as our company NOBLE POSTS ABROAD.WE OFFER JOBS IN ROYAL PALACES SO THE LANDING PAGE SHOULD REFLECT THAT. We have prepared the landing page leading page photo, logo and a landing page structure. We prefer a very classy and elegant page with not much colors - black and white and gray tones is nice with a nice photos. The main photo we have suggested and we will purchase if in case the designer will like it and we agree on the style. Here is the link to it https://www.pixmarketvault.example/ae/photo/beautiful-roses-and-baroque-rococo-style-palace-in-background-gm502938174-3197205 . WE ARE OPEN TO ANY PALACE PHOTO TO ATTRACT APPLICANTS TO US

Target Market(s)

Job Applicants, cleaners, nannies, cooks, nurses, tutors

Industry/Entity Type

Recruitment

Font styles to use
Serif

Requirements
Must have
• The sections that we have suggested. Our current web site if www.prime-homecrew.example you can use the partners logos from here and clients testimonials.
Nice to have
• If you have any other landing main photo that will suit more please suggest. This is only our recommendation and we have limited designers skills :). please we like clean designs - black and white lines and gray tones. Nothing too colorful. Classy and Clean.
Should not have
• We like one color palette, not numerous colors and mixed all together.

```html
<!DOCTYPE html>
<html lang="en">
<head>
<meta charset="UTF-8">
<title>Noble Posts Abroad — Apply</title>
<link href="https://fonts.googleapis.com/css2?family=Poppins:wght@400;500;600;700&family=Open+Sans:wght@400;600&display=swap" rel="stylesheet">
<style>
:root{
  --ink:#111111;
  --text:#2b2b2b;
  --muted:#6f6f6f;
  --line:#d9d9d9;
  --accent:#e59191;
  --panel:#f1f1f1;
  --dark:#231f20;
  --white:#ffffff;
}
*{box-sizing:border-box;margin:0;padding:0}
html,body{width:1200px;height:5255px;overflow:hidden}
body{position:relative;background:var(--white);color:var(--text);font-family:"Open Sans",Arial,sans-serif}
.abs{position:absolute}
.heading{font-family:"Poppins",Arial,sans-serif;font-weight:600;color:var(--ink);text-align:center;width:100%;left:0}
.rule{height:4px;width:138px;background:var(--accent);left:531px;border-radius:2px}

.topbar{top:0;left:0;width:1200px;height:20px;background:var(--dark)}
.nav{top:20px;left:0;width:1200px;height:92px;background:var(--white)}
.brand{position:absolute;left:88px;top:34px;font-family:"Poppins",sans-serif;font-size:12px;letter-spacing:.5px;color:var(--text);display:flex;align-items:center;gap:8px}
.brand .dot{width:10px;height:10px;border-radius:50%;background:var(--text)}
.menu{position:absolute;right:128px;top:48px;display:flex;gap:36px;font-family:"Poppins",sans-serif;font-size:14px;color:var(--text);list-style:none}

.hero{top:112px;left:0;width:1200px;height:503px;background:linear-gradient(180deg,#a9bcd1 0%,#d2dbe4 28%,#c9c2b4 45%,#a79d8c 70%,#6d7a55 88%,#4f5e3b 100%)}

.benefits-title{top:676px;font-size:23px}
.benefit{top:775px;width:140px;text-align:center;font-family:"Poppins",sans-serif;font-size:9px;font-weight:500;color:var(--ink);line-height:1.2}
.benefit svg{display:block;margin:0 auto 10px}

.form-title{top:1000px;font-size:29px}
.apply-head{top:1198px;left:145px;font-family:"Poppins",sans-serif;font-weight:700;font-size:47px;line-height:55px;letter-spacing:1px;color:#333}
.apply-copy{top:1400px;left:145px;width:420px;font-size:19px;line-height:29px;color:#333}
.card{top:1146px;left:701px;width:383px;height:413px;background:var(--white);box-shadow:0 6px 30px rgba(0,0,0,.12)}
.card h3{position:absolute;left:48px;top:48px;font-family:"Poppins",sans-serif;font-size:26px;font-weight:600;color:var(--ink)}
.field{position:absolute;left:48px;width:274px;height:36px;border:1px solid var(--line);box-shadow:0 2px 4px rgba(0,0,0,.06);font-size:11px;color:#888;padding:10px 14px}
.send{position:absolute;left:29px;top:311px;width:311px;height:60px;background:var(--accent);color:var(--white);font-family:"Poppins",sans-serif;font-weight:600;font-size:20px;display:flex;align-items:center;justify-content:center}

.positions-title{top:1775px;font-size:29px}
.roles{top:1914px;list-style:none;font-family:"Poppins",sans-serif;font-size:17px;color:var(--ink)}
.roles li{height:48.5px}

.training{top:2355px;left:0;width:1200px;height:655px;background:radial-gradient(ellipse at 70% 40%,#3c3a35 0%,#26261f 45%,#151811 100%)}
.training h2{position:absolute;left:87px;top:130px;font-family:"Poppins",sans-serif;font-weight:700;font-size:36px;line-height:53px;color:var(--white)}
.training p{position:absolute;left:87px;top:400px;font-family:"Poppins",sans-serif;font-weight:600;font-size:20px;line-height:27px;color:var(--white)}
.learn{position:absolute;left:87px;top:520px;width:184px;height:45px;background:var(--white);color:var(--ink);font-family:"Poppins",sans-serif;font-size:13px;font-weight:500;display:flex;align-items:center;justify-content:center}

.how-title{top:3155px;font-size:36px;font-weight:500}
.step-img{top:3255px;width:258px;height:141px;border-radius:3px}
.step-cap{top:3425px;width:258px;text-align:center;font-size:13px;line-height:21px;color:#444}
.more{top:3535px;left:472px;width:256px;height:60px;border:1px solid var(--line);box-shadow:0 2px 4px rgba(0,0,0,.06);color:var(--accent);font-size:12px;display:flex;align-items:center;justify-content:center}

.partners-title{top:3728px;font-size:29px;font-weight:500}
.partner{top:3825px;height:50px;background:#cfcfcf;border-radius:4px}

.testimonials{top:3995px;left:0;width:1200px;height:495px;background:var(--panel)}
.testimonials h2{position:absolute;top:62px;left:0;width:100%;text-align:center;font-family:"Poppins",sans-serif;font-weight:600;font-size:28px;color:var(--ink)}
.quote-mark{position:absolute;left:178px;top:155px}
.quote{position:absolute;left:276px;top:145px;width:720px;font-size:20px;line-height:29px;color:#333}
.author-rule{position:absolute;left:276px;top:345px;width:100px;height:4px;background:var(--ink)}
.author{position:absolute;left:276px;top:365px;font-family:"Poppins",sans-serif;font-weight:600;font-size:25px;color:var(--ink)}
.author-loc{position:absolute;left:276px;top:402px;font-size:13px;color:#333}
.dots{position:absolute;top:432px;left:540px;display:flex;gap:13px}
.dots span{width:13px;height:13px;border-radius:50%;background:#888}
.dots span:first-child{background:var(--ink)}

.contact-title{top:4590px;left:153px;font-family:"Poppins",sans-serif;font-weight:500;font-size:30px;color:var(--ink)}
.contact-rule{top:4640px;left:153px;width:138px;height:4px;background:var(--accent)}
.label{font-family:"Poppins",sans-serif;font-weight:500;font-size:16px;color:var(--ink)}
.socials{top:4752px;left:173px;display:flex;gap:22px;font-family:"Poppins",sans-serif;font-weight:600;font-size:14px;color:var(--ink)}
.office{font-size:11px;line-height:15px;color:var(--ink);display:flex;gap:16px;align-items:flex-start}
.msg-card{top:4740px;left:765px;width:297px;height:362px;background:var(--white);box-shadow:0 4px 20px rgba(0,0,0,.12)}
.msg-card h4{position:absolute;left:57px;top:38px;font-family:"Poppins",sans-serif;font-weight:600;font-size:14px;color:var(--ink)}
.mlabel{position:absolute;left:38px;font-size:9px;font-weight:600;color:var(--ink)}
.minput{position:absolute;left:38px;width:214px;border:1px solid #cfcfcf;font-size:8px;color:#999;padding:7px 6px}
.msend{position:absolute;left:38px;top:315px;width:112px;height:32px;background:var(--dark);color:var(--white);font-size:10px;display:flex;align-items:center;justify-content:center}

.footer{top:5185px;left:0;width:1200px;height:70px;background:var(--dark);color:var(--white);font-family:"Poppins",sans-serif;font-size:13px}
.footer .copy{position:absolute;left:95px;top:26px}
.footer ul{position:absolute;right:110px;top:26px;display:flex;gap:60px;list-style:none}
</style>
</head>
<body>

<div class="abs topbar"></div>
<header class="abs nav">
  <div class="brand"><span class="dot"></span>NOBLE POSTS ABROAD</div>
  <ul class="menu"><li>About</li><li>Benfits</li><li>How to Apply</li><li>Arrival</li><li>Contact</li></ul>
</header>

<div class="abs hero" role="img" aria-label="Photograph of a grand white stone palace with towers under a cloudy sky, green lawn in front"></div>

<h2 class="abs heading benefits-title">BENEFITS OF WORKING &nbsp;IN ROYAL PALACES</h2>

<div class="abs benefit" style="left:188px">
  <svg width="64" height="64" viewBox="0 0 64 64" fill="none" stroke="#111" stroke-width="2.5"><rect x="8" y="34" width="40" height="20"/><circle cx="28" cy="44" r="5"/><path d="M14 28l12-10 8 6 16-14M42 10h8v8"/></svg>
  SALARY STARTING<br>4000$ NET
</div>
<div class="abs benefit" style="left:328px">
  <svg width="64" height="64" viewBox="0 0 64 64" fill="none" stroke="#111" stroke-width="2.5"><rect x="14" y="14" width="28" height="40" rx="2"/><circle cx="28" cy="32" r="7"/><path d="M21 32h14M28 25v14M42 20l10 4-6 26"/></svg>
  PAID VISA
</div>
<div class="abs benefit" style="left:466px">
  <svg width="64" height="64" viewBox="0 0 64 64" fill="none" stroke="#111" stroke-width="2.5"><circle cx="32" cy="32" r="26"/><circle cx="32" cy="32" r="18"/><path d="M26 20v24M23 20v8h6v-8M38 20v24M38 20c4 2 4 10 0 12"/></svg>
  FOOD &nbsp;AND<br>ACCOMODATION
</div>
<div class="abs benefit" style="left:604px">
  <svg width="64" height="64" viewBox="0 0 64 64" fill="none" stroke="#111" stroke-width="2.5"><rect x="12" y="18" width="28" height="38" rx="2"/><circle cx="26" cy="34" r="7"/><path d="M30 16l20-6 6 24-16 4"/></svg>
  VACATION + TICKET
</div>
<div class="abs benefit" style="left:748px">
  <svg width="64" height="64" viewBox="0 0 64 64" fill="none" stroke="#111" stroke-width="2.5"><rect x="8" y="18" width="48" height="38" rx="3"/><path d="M24 18v-6h16v6M32 28v18M23 37h18"/></svg>
  MEDICAL
</div>
<div class="abs benefit" style="left:870px">
  <svg width="64" height="64" viewBox="0 0 64 64" fill="none" stroke="#111" stroke-width="2.5"><path d="M22 8l-12 8 4 12 6-2v30h24V26l6 2 4-12-12-8-6 6h-8z"/><path d="M32 14v40"/></svg>
  UNIFORMS AND<br>TOILETRIES
</div>

<h2 class="abs heading form-title">FREE APPLICATION FORM</h2>
<div class="abs rule" style="top:1054px"></div>

<h1 class="abs apply-head">APPLY FOR<br>ROYAL JOBS IN<br>DUBAI</h1>
<p class="abs apply-copy">Lorem ipsum dolor sit amet, consectetur adipiscing elit. Vestibulum elementum ullamcorper eros et faucibus.</p>

<form class="abs card">
  <h3>Apply Now</h3>
  <div class="field" style="top:108px">full name</div>
  <div class="field" style="top:168px">email address</div>
  <div class="field" style="top:228px">mobile</div>
  <div class="send">SEND</div>
</form>

<h2 class="abs heading positions-title">POSITIONS WE &nbsp;ARE HIRING</h2>
<div class="abs rule" style="top:1830px"></div>
<ul class="abs roles" style="left:143px"><li>Nannies</li><li>Chambermaid</li><li>Maternity Nurses</li><li>Butlers</li><li>House Managers</li><li>Personal Trainners</li></ul>
<ul class="abs roles" style="left:480px"><li>Estate Managers</li><li>Housekeepers</li><li>Private Chefs</li><li>Governess</li><li>Private Personal Assistants</li><li>Tutors</li></ul>
<ul class="abs roles" style="left:817px"><li>Executive Assitants</li><li>Security Staff</li><li>Yatcht Crew</li><li>Private Jet Cabin Crew</li><li>Chauffeurs</li></ul>

<section class="abs training" role="img" aria-label="Dark photograph of a man in a black suit with a white tie and a rose boutonniere">
  <h2>FREE TRAINING PROGRAMS<br>FOR THE APPLICANTS WHO<br>WISH TO UPGRADE THEIR<br>SKILLSET</h2>
  <p>FREE CERTIFICATION<br>PROGRAMS</p>
  <div class="learn">Learn More</div>
</section>

<h2 class="abs heading how-title">HOW TO APPLY</h2>
<div class="abs step-img" style="left:162px;background:linear-gradient(135deg,#5a7a92,#c9d3dc 55%,#eef0f2)" role="img" aria-label="Photo of a hand signing a document"></div>
<div class="abs step-img" style="left:470px;background:linear-gradient(135deg,#2a2a2a,#7a2b2b 45%,#3a3a3a)" role="img" aria-label="Photo of a red hiring sign in a window"></div>
<div class="abs step-img" style="left:778px;background:linear-gradient(180deg,#8fa3b3,#c6cfd6 50%,#4b4f4f)" role="img" aria-label="Photo of an airport window with a plane outside"></div>
<p class="abs step-cap" style="left:162px">Free joining Visa and Ticket</p>
<p class="abs step-cap" style="left:470px">Applicants will never be charged<br>free application &amp; arrival</p>
<p class="abs step-cap" style="left:778px">Free Safety Landing own butler<br>will welcome at the airport and<br>free airport transfer</p>
<div class="abs more">CLICK &nbsp;FOR MORE DETAILS</div>

<h2 class="abs heading partners-title">OUR PARTNERS</h2>
<div class="abs partner" style="left:175px;width:125px"></div>
<div class="abs partner" style="left:318px;width:120px"></div>
<div class="abs partner" style="left:458px;width:40px"></div>
<div class="abs partner" style="left:518px;width:118px"></div>
<div class="abs partner" style="left:655px;width:98px"></div>
<div class="abs partner" style="left:773px;width:125px"></div>
<div class="abs partner" style="left:915px;width:110px"></div>

<section class="abs testimonials">
  <h2>WHAT OUR CLIENT SAY ABOUT US</h2>
  <svg class="quote-mark" width="56" height="36" viewBox="0 0 56 36" fill="#111"><circle cx="12" cy="12" r="11"/><path d="M22 12c0 12-8 20-18 23l-1-4c7-3 11-9 11-17z"/><circle cx="40" cy="12" r="11"/><path d="M50 12c0 12-8 20-18 23l-1-4c7-3 11-9 11-17z"/></svg>
  <p class="quote">Lorem ipsum dolor sit amet, consectetur adipiscing elit. Vestibulum elementum ullamcorper eros et faucibus. Cras blandit id velit eu dignissim. Aenean ac eleifend est. Nunc tristique leo eget justo feugiat, vitae venenatis augue suscipit. Phasellus sodales massa non nibh imperdiet bibendum.</p>
  <div class="author-rule"></div>
  <p class="author">Maren T., Irish</p>
  <p class="author-loc">Based in Dubai</p>
  <div class="dots"><span></span><span></span><span></span><span></span><span></span></div>
</section>

<h2 class="abs contact-title">CONTACT &nbsp;US</h2>
<div class="abs contact-rule"></div>
<p class="abs label" style="top:4698px;left:173px">FOLLOW US</p>
<div class="abs socials"><span>Chirper</span><span>Pagebook</span><span>Snapline</span><span>Linkwork</span><span>Plusnet</span></div>
<p class="abs label" style="top:4870px;left:173px">OUR OFFICES</p>

<div class="abs office" style="top:4928px;left:175px">
  <svg width="16" height="20" viewBox="0 0 16 20" fill="none" stroke="#111" stroke-width="2"><path d="M8 19s6-7 6-11A6 6 0 0 0 2 8c0 4 6 11 6 11z"/><circle cx="8" cy="8" r="2"/></svg>
  <span>Cedar Tower 9th street<br>Ash Lane, Dubai, UAE</span>
</div>
<div class="abs office" style="top:4928px;left:422px">
  <svg width="16" height="20" viewBox="0 0 16 20" fill="none" stroke="#111" stroke-width="2"><path d="M8 19s6-7 6-11A6 6 0 0 0 2 8c0 4 6 11 6 11z"/><circle cx="8" cy="8" r="2"/></svg>
  <span>Linden House, 4th street<br>London, UK</span>
</div>
<div class="abs office" style="top:4978px;left:177px">
  <svg width="12" height="20" viewBox="0 0 12 20" fill="none" stroke="#111" stroke-width="2"><rect x="1" y="1" width="10" height="18" rx="2"/><path d="M5 16h2"/></svg>
  <span style="padding-top:3px">00 555010477</span>
</div>
<div class="abs office" style="top:4975px;left:423px">
  <svg width="12" height="20" viewBox="0 0 12 20" fill="none" stroke="#111" stroke-width="2"><rect x="1" y="1" width="10" height="18" rx="2"/><path d="M5 16h2"/></svg>
  <span style="padding-top:3px">00 555010477</span>
</div>
<div class="abs office" style="top:5045px;left:175px;gap:24px">
  <svg width="18" height="30" viewBox="0 0 18 30" fill="none" stroke="#111" stroke-width="2.5"><rect x="2" y="2" width="14" height="26" rx="3"/><path d="M7 24h4"/></svg>
  <span style="padding-top:8px">00 555010477</span>
</div>
<div class="abs office" style="top:5052px;left:422px;gap:30px">
  <svg width="34" height="22" viewBox="0 0 34 22" fill="#111"><path d="M0 0h34v22H0z"/><path d="M2 2l15 11L32 2" stroke="#fff" stroke-width="2" fill="none"/></svg>
  <span style="padding-top:4px">info@nobleposts.example</span>
</div>

<form class="abs msg-card">
  <h4>SEND US A MESSAGE</h4>
  <span class="mlabel" style="top:72px">Name</span>
  <div class="minput" style="top:87px;height:26px">eg. Adam Reyes</div>
  <span class="mlabel" style="top:128px">Email</span>
  <div class="minput" style="top:143px;height:26px">eg. yourname@mail.example</div>
  <span class="mlabel" style="top:188px">Message</span>
  <div class="minput" style="top:203px;height:68px"></div>
  <div class="msend">Send</div>
</form>

<footer class="abs footer">
  <span class="copy">All rights Reserved. 2020. Noble Posts Abroad</span>
  <ul><li>Terms of use</li><li>Privacy</li><li>Contact</li></ul>
</footer>

</body>
</html>
```